Postcard Design

Hoofmere Ftness Center is a state of the art equine rehabilitation and fitness center. We offer a wide variety of options to get your equine partner in tip top performing condition. Whether is swimming in or 11 foot deep pool or exercising in the squatted, we provide a personalized program for your special horse. Some other services offered are StallAir breathing treatments, pulso drift and gallotone.
Updates
Project Deadline Extended Reason: Since the project was started we have opened for business and I have pictures using my equipment at our place of business that I would like to add to the project to be used. I have also received my logo design from one of your designers that I would like added to this project. Added Tuesday, March 15, 2016
Industry/Entity Type
Fitness
Look and feel
Each slider illustrates characteristics of the customer's brand and the style your logo design should communicate.

```html
<!DOCTYPE html>
<html lang="en">
<head>
<meta charset="UTF-8">
<title>Hoofmere Ftness Center – Postcard</title>
<link rel="stylesheet" href="https://fonts.googleapis.com/css2?family=Dancing+Script:wght@500&family=Quicksand:wght@500&family=Roboto:wght@400&display=swap">
<style>
  :root {
    --canvas-bg: #e9e6e2;
    --card-bg: #ffffff;
    --brand-teal: #1f9aa8;
    --ink: #1a1a1a;
    --panel-black: #000000;
    --panel-text: #ffffff;
    --rule: #555555;
    --art-gradient: linear-gradient(135deg, #0b0b0b 0%, #0b0b0b 30%, #2bb3c8 45%, #f2c12e 55%, #d2305a 65%, #6a3fb0 75%, #2fb07a 88%, #0b0b0b 100%);
    --photo-gradient: linear-gradient(180deg, #8a7a66 0%, #6f6253 28%, #3aa6ad 45%, #6fd0d3 75%, #2c8f99 100%);
  }
  * { margin: 0; padding: 0; box-sizing: border-box; }
  html, body { width: 960px; height: 1200px; overflow: hidden; }
  body { background: var(--canvas-bg); position: relative; }

  .postcard { position: absolute; background: var(--card-bg); box-shadow: 0 4px 14px rgba(0,0,0,0.18); }

  /* Front side */
  .postcard-front { left: 77px; top: 38px; width: 697px; height: 536px; }
  .front-artwork { position: absolute; left: 9px; top: 10px; width: 679px; height: 406px; background: var(--art-gradient); }
  .front-title {
    position: absolute; left: 0; right: 0; top: 440px; text-align: center;
    font-family: "Dancing Script", cursive; font-weight: 500; font-size: 62px;
    color: var(--brand-teal); line-height: 1;
  }

  /* Back side */
  .postcard-back { left: 190px; top: 618px; width: 694px; height: 534px; }
  .back-title {
    position: absolute; left: 10px; width: 324px; top: 12px; text-align: center;
    font-family: "Dancing Script", cursive; font-weight: 500; font-size: 25px;
    color: var(--brand-teal); line-height: 24px;
  }
  .back-intro {
    position: absolute; left: 10px; width: 324px; top: 80px; text-align: center;
    font-family: "Quicksand", sans-serif; font-weight: 500; font-size: 12.5px;
    color: var(--ink); line-height: 15px;
  }
  .back-photo { position: absolute; left: 10px; top: 114px; width: 324px; height: 254px; background: var(--photo-gradient); }
  .services-panel {
    position: absolute; left: 10px; top: 368px; width: 324px; height: 156px;
    background: var(--panel-black); color: var(--panel-text);
    font-family: "Roboto", sans-serif; font-size: 12px; line-height: 15px;
    padding: 8px 11px;
  }
  .services-panel p { text-align: justify; }
  .services-panel .services-lead { margin-top: 6px; }
  .services-list { list-style: none; }
  .services-list li::before { content: "•"; margin-right: 6px; }

  .stamp-box { position: absolute; left: 583px; top: 28px; width: 82px; height: 78px; border: 1px solid var(--rule); }
  .address-lines { position: absolute; left: 391px; top: 174px; width: 274px; }
  .address-lines span { display: block; height: 1px; background: var(--rule); margin-bottom: 35px; }
</style>
</head>
<body>
  <section class="postcard postcard-front">
    <div class="front-artwork" role="img" aria-label="Colourful painted illustration of a horse head with a flowing rainbow mane on black"></div>
    <h1 class="front-title">Hoofmere Ftness Center</h1>
  </section>

  <section class="postcard postcard-back">
    <h2 class="back-title">Hoofmere<br>Ftness Center</h2>
    <p class="back-intro">Hoofmere Ftness Center is a state of the art equine<br>rehabilitation and fitness center.</p>
    <div class="back-photo" role="img" aria-label="Photo of a dark horse being exercised in a swimming pool"></div>
    <div class="services-panel">
      <p>We offer a wide variety of options to get your equine partner in tip top performing condition. Whether is swimming in or 11 foot deep pool or exercising in the squatted, we provide a personalized program for your special horse.</p>
      <p class="services-lead">Some other services offered are:</p>
      <ul class="services-list">
        <li>StallAir breathing treatments</li>
        <li>Pulso drift</li>
        <li>Gallotone</li>
      </ul>
    </div>
    <div class="stamp-box"></div>
    <div class="address-lines"><span></span><span></span><span></span><span></span><span></span></div>
  </section>
</body>
</html>
```